Marketing / Informational Site for Marriage and Family Therapists Cooperative

We need a web design for a new Marriage and Family Therapist Cooperative, called Meadowgate Counselors. This is a market and information site for potential clients and referrals to learn more about the team and get contact information.

We are looking for profession, clean, and modern design, that cater towards families and mom's concerned about their families mental health and child development.

This should include a home page, an general about page, 3 bio pages (1 for each therapist listed below), and a general contact us page.

Our Domain Name

Meadowgatecounselors.example

Company Name

Meadowgate Counselors

Group Moto/Philosophy

“Our sorrows and wounds are healed only when we touch them with compassion.” - Orvelan

Our Logo

See Heron Final (attached)

Home Page (Introduction)

Feeling stressed and overwhelmed?
Encountering barriers towards your goals?
Having difficulty accomplishing the simplest task?
Have the need to talk but unsure who to turn to?

Therapy can assist you in overcoming all of these challenges. Assist you in uncovering the difficulties and barriers that are keeping you from achieving your life’s ambitions, help discover ways to overcome them, and cope with the impact your behaviour has on your occupation, personal life and social life.

Welcome to our practice, with over 20 years of combined experience in the clinical field you are sure to find the right fit for your needs. Each clinician has experience working with groups, adults, teens, children, families, and couples. We specialize in fostering healthy relationships between individuals, managing depression and anxiety, overcoming trauma, and developing occupational success. Feel free to explore information about each clinician and make an appointment with one of us today.

About Us (bio pics attached)

Marisel Dunkworth

My name is Dr. MariSel Dunkworth and I am a Licensed Marriage Family Therapist with a practice in Riverside, CA. I have devoted my life’s work into developing my skills in this profession. I have over 15 years of experience working in the clinical and the social service settings. These years have afforded me the opportunity to work with groups, families, adults, teens and children with varying symptoms. I have helped clients that have trauma, abuse histories, and many within the legal or social service systems. I enjoy working individuals from all walks of life achieve self sufficiency, social success and occupational success. In my years of training I have come to develop a culturally sensitive practice that centers around the needs of the client.

I have held many positions in my clinical career beginning as clinician moving upwards toward supervisor and program coordinator. I have also over 5 years of experience as an adjunct faculty member in the University setting teaching student to become Marriage and Family Therapists. As a clinician I focused on enriching my clinical skills by developing outcome driven practices to achieve client’s desired goals. As a clinical supervisor, I guided clinicians along their own paths towards clinical licensure. As a program coordinator, I helped develop a clinical assessment and triage program from ground up to assist client in accessing services in the South Los Angeles Area. The program would assist over 100 plus clients on a monthly basis get connected to clinical services and linked to any additional resources as needed by the individual. I have graduated with my, Bachelor’s degree at the Halvern College, Riverside. I received my Masters degree in Clinical Psychology at Mount St. Mary’s University, and my Doctorate degree in Clinical Psychology at Tamsworth Institute.

To schedule an appointment with Dr. MariSel Dunkworth, LMFT:

email: marisel582@postbox.example
Phone: (951)555-0182

Jeb Kowal

My name is Rosalindra (Jeb) Kowal, I received my Masters Degree of Counseling in Marriage and Family Therapy from Corvell Bay State College in June 2000. I have acquired over 15 years of experience helping Individuals, Couples, and Families cope with issues of Anxiety, Depression, Grief and Bereavement, and HIV/AIDS.

I am a Family Systems Therapist and I truly believe the dynamics in our family of origin greatly shape our current belief systems and behaviors. However, I often utilize a variety of approaches to help my clients achieve their goals depending on their individual needs.

My greatest strength as a Marriage and Family Therapist is helping my clients explore ways to make the changes in their lives that will allow them to live their life to their fullest potential. I help my clients achieve their personal life goals with a warm, safe, non-judgmental , and supportive environment. In doing so, my clients are encouraged to explore the issues that may be preventing them from living the life they desire. Thus, empowering them to take control of their personal journey to living a productive and meaningful life.

If you feel that you are ready to commit to bringing about positive changes in your life and would like support in exploring this path, I’m here to work with you in your journey to personal growth and development.

To schedule an appointment with Rosalindra Kowal, LMFT:

e-mail: rkjeb7@mailnest.example
Phone: (951)555-0147

Dena Holcroft

Dena Holcroft graduated with a Masters in Marriage and Family Therapy from Pellridge Crestwood College. She currently holds a license in Marriage and Family Therapy in the State of California. She is also formally trained in Clinical Art Therapy. Dena's expertise lies in providing treatment to individuals experiencing work-related injuries, severe physical and emotional pain, trauma, grief and loss, anxiety and depression. In her early career, she provided valuable service at the largest free clinic in the nation serving marginalized families and children. For the past ten years, Dena has worked with HIV/AIDS population.
Dena comes from a multicultural background and she has utilized this experience and knowledge in serving a variety of populations. At an organizational level, Dena has worked extensively with challenging issues such as the chemical dependency and homelessness. In her private practice, Dena is proficient in working within individuals experiencing relationship concerns, marital and family conflict, depression/anxiety, self-esteem concerns, adjustment disorders, and pain management. She has treated clients from diverse cultural, linguistic backgrounds and sexual orientations.
Dena is trained in Family Systems Theory and incorporates other strategies appropriate for each presenting issue. She specializes in Clinical Art Therapy and has successfully utilized an integrated approach including guided imagery and relaxation skills training for many years.

To schedule an appointment with Dena Holcroft, LMFT

e-mail: greypinestudio@inkmail.example
Phone: (951) 555-0169

Target Market(s)

Families with child development, marriage issues, or other mental health needs

Industry/Entity Type

Marketing

Number of Pages Required

5+ page

Requirements
Must have
• 1 home page, 1 about page, 1 contact page. About page could either be standalone page with 3 different bio pages for each therapist or an all in one about page that includes bios for all 3 therapists.

```html
<!DOCTYPE html>
<html lang="en">
<head>
<meta charset="utf-8">
<title>Meadowgate Counselors</title>
<link href="https://fonts.googleapis.com/css2?family=Open+Sans:wght@400;600;700&family=Lora:ital@1&display=swap" rel="stylesheet">
<style>
:root{
  --green:#5cbf8f;
  --green-dark:#3f9f74;
  --teal:#1fa6a0;
  --orange:#f39a1f;
  --text:#4a4a4a;
  --muted:#8a8a8a;
  --line:#dcdcdc;
  --panel:#f3f3f3;
  --footer:#e9ecee;
}
*{box-sizing:border-box;margin:0;padding:0}
html,body{width:789px;height:1200px;overflow:hidden}
body{font-family:"Open Sans",Arial,sans-serif;color:var(--text);background:#dfe3e5;font-size:11px}
.page{position:relative;width:789px;height:1200px;background:#fff;overflow:hidden}

.site-header{position:absolute;left:0;top:0;width:789px;height:88px}
.brand{position:absolute;left:26px;top:24px;display:flex;align-items:center;gap:8px;color:var(--green);font-weight:600;font-size:15px}
.brand-dot{width:26px;height:26px;border-radius:50%;background:var(--green)}
.social{position:absolute;left:520px;top:20px;display:flex;gap:5px}
.social span{width:20px;height:20px;border-radius:50%;background:var(--teal)}
.btn-schedule{position:absolute;left:615px;top:20px;width:150px;height:22px;background:var(--teal);color:#fff;font-size:9px;font-weight:600;text-align:center;line-height:22px}
.nav{position:absolute;left:530px;top:56px;display:flex;gap:4px;font-size:9px;font-weight:700}
.nav a{padding:5px 9px;color:var(--text);text-decoration:none}
.nav a.active{background:var(--green);color:#fff}

.hero{position:absolute;left:0;top:88px;width:789px;height:346px;background:linear-gradient(180deg,#8fb3c4 0%,#c9c3a6 45%,#f2b764 70%,#3c3626 100%)}
.hero-quote{position:absolute;left:26px;top:120px;width:240px;color:#fff;font-family:"Lora",Georgia,serif;font-style:italic;font-size:17px;line-height:1.4}
.hero-quote cite{display:block;margin-top:10px;font-size:13px}
.dots{position:absolute;left:380px;top:318px;display:flex;gap:6px}
.dots span{width:7px;height:7px;border-radius:50%;background:rgba(255,255,255,.6)}
.dots span:first-child{background:#fff}

.schedule{position:absolute;left:0;top:434px;width:789px;height:250px;background:#fff}
.section-title{text-align:center;color:var(--green);font-weight:700;font-size:19px;letter-spacing:.5px}
.schedule .section-title{margin-top:22px}
.tabs{position:absolute;left:55px;top:66px;display:flex;font-size:10px;font-weight:600}
.tabs span{height:22px;line-height:22px;padding:0 20px;background:#f3f3f3;color:var(--teal)}
.tabs .label{background:var(--teal);color:#fff}
.tabs .active{background:var(--orange);color:#fff}
.form-panel{position:absolute;left:55px;top:88px;width:680px;height:146px;background:var(--panel);border-top:3px solid var(--orange)}
.photo{position:absolute;left:12px;top:12px;width:100px;height:120px;background:linear-gradient(#d9cfc5,#9d8f82)}
.photo-label{position:absolute;left:0;bottom:0;width:100%;background:var(--teal);color:#fff;font-size:8px;padding:3px 5px}
.field{position:absolute;height:20px;background:#fff;border:1px solid var(--line);font-size:8px;color:var(--muted);padding:5px 6px}
.btn{position:absolute;height:20px;font-size:8px;font-weight:700;color:#fff;text-align:center;line-height:20px}

.welcome{position:absolute;left:0;top:684px;width:789px}
.welcome .section-title{margin-top:22px}
.welcome .section-title em{font-style:normal;color:var(--orange)}
.questions{position:absolute;left:30px;top:80px;width:729px;display:grid;grid-template-columns:1fr 1fr;gap:12px 24px}
.q{display:flex;align-items:center;gap:10px;height:36px;border:1px solid var(--line);padding:0 10px;font-weight:700;font-size:11.5px;color:#555}
.q svg{flex:none}
.copy{position:absolute;left:30px;top:200px;width:729px;font-size:9.5px;line-height:1.55;color:var(--muted)}
.copy p+p{margin-top:10px}
.cta{position:absolute;top:330px;display:flex;gap:10px;left:278px}
.cta span{background:var(--green);color:#fff;font-size:9px;font-weight:700;padding:7px 14px}

.site-footer{position:absolute;left:0;top:1078px;width:789px;height:122px;background:var(--footer);font-size:8px;color:var(--muted);line-height:1.55}
.fcol{position:absolute;top:18px}
.fcol h4{font-size:9px;color:var(--text);margin-bottom:4px}
.fbrand{position:absolute;left:630px;top:44px;color:var(--green);font-size:11px;font-weight:600}
</style>
</head>
<body>
<div class="page">
  <header class="site-header">
    <div class="brand"><span class="brand-dot"></span>Meadowgate Counselors</div>
    <div class="social"><span></span><span></span><span></span></div>
    <div class="btn-schedule">SCHEDULE AN APPOINTMENT</div>
    <nav class="nav"><a class="active">HOME</a><a>ABOUT</a><a>THERAPISTS</a><a>CONTACT</a></nav>
  </header>

  <section class="hero" role="img" aria-label="Photograph of a family in silhouette holding hands against a sunset sky">
    <blockquote class="hero-quote">“Our sorrows and wounds are healed only when we touch them with compassion.”<cite>- Orvelan</cite></blockquote>
    <div class="dots"><span></span><span></span><span></span><span></span></div>
  </section>

  <section class="schedule">
    <h2 class="section-title">SCHEDULE AN APPOINTMENT</h2>
    <div class="tabs">
      <span class="label">THERAPIST</span>
      <span class="active">Dr. Marisel Dunkworth</span>
      <span>Jeb Kowal</span>
      <span>Dena Holcroft</span>
    </div>
    <div class="form-panel">
      <div class="photo" role="img" aria-label="Portrait photo of the therapist"><div class="photo-label">View Profile</div></div>
      <div class="field" style="left:126px;top:16px;width:150px">First Name</div>
      <div class="field" style="left:290px;top:16px;width:150px">Email</div>
      <div class="field" style="left:126px;top:48px;width:150px">Last Name</div>
      <div class="field" style="left:290px;top:48px;width:150px">Desired Date</div>
      <div class="field" style="left:126px;top:80px;width:150px">Phone Number</div>
      <div class="field" style="left:290px;top:80px;width:150px">Desired Hour</div>
      <div class="field" style="left:454px;top:16px;width:214px;height:54px">Message / Comment</div>
      <div class="btn" style="left:510px;top:80px;width:60px;background:var(--orange)">SUBMIT</div>
      <div class="btn" style="left:580px;top:80px;width:60px;background:var(--orange)">RESET</div>
    </div>
  </section>

  <section class="welcome">
    <h2 class="section-title">WELCOME TO <em>MEADOWGATE COUNSELORS</em></h2>
    <div class="questions">
      <div class="q"><svg width="18" height="18" viewBox="0 0 18 18"><circle cx="9" cy="9" r="8" fill="none" stroke="#888" stroke-width="1.5"/><path d="M9 5v5M9 12.5v1" stroke="#888" stroke-width="1.6"/></svg>Feeling stressed and overwhelmed?</div>
      <div class="q"><svg width="18" height="18" viewBox="0 0 18 18"><rect x="2" y="2" width="14" height="14" fill="none" stroke="#888" stroke-width="1.5"/><path d="M5 9l3 3 5-6" fill="none" stroke="#888" stroke-width="1.6"/></svg>Having difficulty accomplishing the simplest task?</div>
      <div class="q"><svg width="18" height="18" viewBox="0 0 18 18"><circle cx="9" cy="9" r="8" fill="none" stroke="#888" stroke-width="1.5"/><circle cx="9" cy="9" r="4" fill="none" stroke="#888" stroke-width="1.5"/></svg>Encountering barriers towards your goals?</div>
      <div class="q"><svg width="18" height="18" viewBox="0 0 18 18"><path d="M2 3h14v9H7l-4 3v-3H2z" fill="none" stroke="#888" stroke-width="1.5"/></svg>Have the need to talk but unsure who to turn to?</div>
    </div>
    <div class="copy">
      <p>Therapy can assist you in overcoming all of these challenges. Assist you in uncovering the difficulties and barriers that are keeping you from achieving your life’s ambitions, help discover ways to overcome them, and cope with the impact your behaviour has on your occupation, personal life and social life.</p>
      <p>Welcome to our practice, with over 20 years of combined experience in the clinical field you are sure to find the right fit for your needs. Each clinician has experience working with groups, adults, teens, children, families, and couples. We specialize in fostering healthy relationships between individuals, managing depression and anxiety, overcoming trauma, and developing occupational success. Feel free to explore information about each clinician and make an appointment with one of us today.</p>
    </div>
    <div class="cta"><span>LEARN MORE</span><span>VIEW OUR THERAPISTS</span></div>
  </section>

  <footer class="site-footer">
    <div class="fcol" style="left:30px"><h4>Navigation</h4>Home<br>Therapists<br>Contact Us</div>
    <div class="fcol" style="left:150px"><h4>Contact</h4>Dr. Marisel Dunkworth<br>Phone: (951)555-0182<br>marisel582@postbox.example</div>
    <div class="fcol" style="left:300px"><h4>&nbsp;</h4>Jeb Kowal<br>Phone: (951)555-0147<br>rkjeb7@mailnest.example</div>
    <div class="fcol" style="left:450px"><h4>&nbsp;</h4>Dena Holcroft<br>Phone: (951) 555-0169<br>greypinestudio@inkmail.example</div>
    <div class="fbrand">Meadowgate Counselors</div>
  </footer>
</div>
</body>
</html>
```